Plot Lantern Website Design

At Plot Lantern we’re about to launch an exciting new product in the Project Management space. We aim to simplify the process of reporting on-site work activities. Our flagship product, Briskline, provides users the ability to record work activities as they are performed with automatic reporting back to home base using a smartphone.
The website will be the primary face of the company, and is to be used for advertising the product, for sales, and for subscribers to manage their data. We need a site with a clean, simple appearance that is easy to navigate. To give you a better idea of what we need, our brief includes a wire frame template for the site.
We’d like you to produce a single page site design as shown in the wireframe. We’re looking for a Web 2.0 design and can implement any animation effects that your design needs, just provide us with some notes on how each element should behave. You’re free to design whatever you like within the bounds set out below. After the design is complete the team at Plot Lantern will turn it into a functional website.
-Logo provided. We’d like the website to adhere to work with the logo either using the same colour theme (blue, black, grey) or one you think is complementary.
-Site design to include logo and ‘PlotLantern’ as title at the top of the page.
-Use suitable stock images when you need to place an image.
-Ensure you provide links for the images you use so we can purchase them if we choose.
-Link to hero image example http://www.framevaultpics.example/photo/worker-holding-handset-at-factory-yard-58193047. We aren’t completely happy with this image so we’re open for suggestions of superior images.
-Styling for all visual aspects of the site, including colors, font selection, sizing, placement, shadowing, backgrounds, images, layout, etc.
-Styling of text boxes, ie user login, sign up etc.
-‘Site map’ links at the bottom of page
-Styled form for user sign up, modal acceptable.
link to the Orbix App Bazaar.
-Site may need to be responsive to screen size, mobile, tablet, desktop. Aim for desktop but consider other formats. Styling to accomodate. Please use a standardised grid system.
Target Market(s)
Construction professionals, ie Contract Administrators, Project Managers and trades people
Industry/Entity Type
Advertising
Requirements
Must have
- See brief above
Nice to have
- See brief above
Should not have
- See brief above

```html
<!DOCTYPE html>
<html lang="en">
<head>
<meta charset="utf-8">
<title>Plot Lantern</title>
<link href="https://fonts.googleapis.com/css2?family=Lato:wght@400;700&family=Roboto:wght@400;500;700&display=swap" rel="stylesheet">
<style>
:root{
  --blue:#1a6fc1;
  --blue-dark:#0f5aa3;
  --ink:#222;
  --text:#444;
  --muted:#999;
  --line:#d4d4d4;
  --panel:#efefef;
  --footer:#3a3a3a;
  --footer-base:#2a2a2a;
  --white:#fff;
}
*{box-sizing:border-box;margin:0;padding:0}
html,body{width:1200px;height:2334px;overflow:hidden}
body{position:relative;font-family:"Lato",sans-serif;color:var(--text);background:var(--white)}
.abs{position:absolute}
a{color:inherit;text-decoration:none}

/* header */
.site-header{left:0;top:0;width:1200px;height:90px;background:var(--white)}
.brand{left:161px;top:20px;display:flex;align-items:center;gap:12px}
.brand-mark{width:40px;height:40px;background:var(--blue)}
.brand-name{font-family:"Roboto",sans-serif;font-weight:700;font-size:38px;color:var(--blue);letter-spacing:-.5px}
.field-sm{height:24px;border:1px solid #c8c8c8;background:var(--white);font-size:9px;color:var(--muted);padding:6px 8px;line-height:10px}
.btn-sm{height:24px;background:var(--blue);color:var(--white);font-size:10px;font-weight:700;text-align:center;line-height:24px}
.nav{top:58px;right:0;left:0;height:20px;font-family:"Roboto",sans-serif;font-size:13px;color:#555}
.nav span{position:absolute}
.nav span::after{content:" \25BE";font-size:8px;color:#aaa}

/* hero */
.hero{left:0;top:90px;width:1200px;height:589px;background:linear-gradient(180deg,#5d8bc4 0%,#8fb2dc 45%,#c8d9ec 100%)}
.hero-band{left:0;top:527px;width:1200px;height:152px;background:rgba(26,111,193,.92)}
.hero-title{left:0;top:558px;width:1200px;text-align:center;font-family:"Roboto",sans-serif;font-weight:500;font-size:30px;line-height:42px;color:var(--white);text-transform:uppercase}
.hero-arrow{top:367px;width:32px;height:32px;border-radius:50%;background:rgba(255,255,255,.9)}

/* welcome */
.section-title{font-family:"Roboto",sans-serif;font-weight:700;color:var(--blue)}
.welcome-title{left:0;top:716px;width:1200px;text-align:center;font-size:25px}
.title-rule{height:1px;background:var(--line)}
.welcome-copy{left:163px;top:768px;width:870px;font-size:12.5px;line-height:20px;text-align:center;color:#555}
.btn-outline{left:543px;top:856px;width:115px;height:31px;border:2px solid #333;border-radius:3px;font-size:13px;font-weight:700;color:#222;text-align:center;line-height:27px}

/* signup + video */
.work-band{left:0;top:932px;width:1200px;height:338px;background:linear-gradient(180deg,#3a3a38,#242422)}
.signup-panel{left:161px;top:976px;width:424px;height:269px;background:rgba(18,18,18,.9)}
.signup-title{left:161px;top:1032px;width:424px;text-align:center;font-family:"Roboto",sans-serif;font-weight:500;font-size:19px;color:var(--white)}
.signup-input{left:237px;top:1070px;width:278px;height:35px;background:var(--white);border-radius:2px;font-size:10px;color:var(--muted);padding:12px 10px}
.btn-primary{background:var(--blue);color:var(--white);font-weight:700;text-align:center;border-radius:3px}
.signup-btn{left:313px;top:1128px;width:126px;height:37px;line-height:37px;font-size:15px}
.video{left:611px;top:976px;width:428px;height:245px;background:linear-gradient(160deg,#8aa0b6 0%,#c7a23a 45%,#6f6656 100%)}
.video-title{left:611px;top:1032px;width:428px;text-align:center;font-family:"Roboto",sans-serif;font-weight:700;font-size:20px;color:var(--white)}
.video-bar{left:611px;top:1194px;width:428px;height:27px;background:#111}

/* quick links strip */
.link-strip{left:0;top:1270px;width:1200px;height:127px;background:linear-gradient(180deg,#f7f7f7,#dedede);border-top:1px solid #ccc;border-bottom:1px solid #ccc}
.strip-btn{top:1313px;width:158px;height:45px;border-radius:3px;font-family:"Roboto",sans-serif;font-size:14px;font-weight:500;color:var(--white);text-align:center;line-height:45px;background:linear-gradient(180deg,#2a84d6,var(--blue-dark))}
.store-btn{left:161px;background:#111;display:flex;align-items:center;gap:8px;padding-left:14px;text-align:left;line-height:1}
.store-icon{width:16px;height:16px;background:var(--white)}
.store-btn b{display:block;font-size:14px}
.store-btn small{display:block;font-size:8px;margin-top:2px;font-weight:400}

/* features + form */
.feature-area{left:0;top:1397px;width:1200px;height:482px;background:var(--panel)}
.feature-title{left:161px;top:1440px;font-size:22px}
.tile{width:200px;height:155px}
.tile-caption{position:absolute;left:0;bottom:0;width:100%;height:18px;background:var(--blue);color:var(--white);font-size:11px;font-weight:700;padding:3px 8px}
.tile-text{left:387px;top:1675px;width:200px;height:155px;background:var(--blue);color:var(--white);padding:10px 14px;font-size:11px;line-height:15px}
.tile-text b{display:block;font-size:12px;margin-bottom:6px}
.tile-text .more{display:block;margin-top:12px;font-weight:700;font-size:12px}
.progress{left:611px;top:1445px;width:428px;height:33px;border:1px solid var(--blue);background:var(--white)}
.progress-fill{left:611px;top:1445px;width:134px;height:33px;background:repeating-linear-gradient(135deg,#1a6fc1 0 10px,#2f80cc 10px 20px);color:var(--white);font-weight:700;font-size:15px;padding:8px 26px}
.form-label{left:611px;width:128px;text-align:right;font-size:11px;color:#444}
.form-field{left:760px;width:279px;height:29px;background:var(--white);border:1px solid #d0d0d0;font-size:9px;color:#aaa;padding:9px 8px}
.callback{left:760px;top:1643px;font-size:11px;color:#444}
.callback i{display:inline-block;width:12px;height:12px;border:1px solid #aaa;margin-left:6px;vertical-align:-2px}
.select-caret{right:0;top:0;width:28px;height:27px;background:#ccc}
.submit-btn{left:611px;top:1788px;width:428px;height:45px;line-height:45px;font-size:15px}

/* testimonials */
.customers-title{left:0;top:1925px;width:1200px;text-align:center;font-size:23px}
.avatar{left:315px;top:1988px;width:74px;height:74px;border-radius:50%;border:3px solid #e5e5e5;background:linear-gradient(180deg,#d8dde4,#aeb7c2)}
.quote{left:408px;top:1986px;width:506px;font-size:12px;line-height:19px;color:#444}
.quote b{display:block;margin-top:6px;color:#222}
.chev{top:2008px}

/* footer */
.site-footer{left:0;top:2124px;width:1200px;height:181px;background:var(--footer)}
.foot-col{top:2150px;color:#ddd}
.foot-col h4{font-family:"Roboto",sans-serif;font-weight:400;font-size:14px;color:#eee;margin-bottom:10px}
.foot-col li{list-style:none;font-size:11px;line-height:21px;color:#ccc}
.foot-col li::before{content:"\2192";margin-right:10px;color:#eee}
.social{top:2152px;left:759px;display:flex;gap:12px}
.social i{width:18px;height:18px;border-radius:50%;background:#2b7fd0}
.foot-about{left:759px;top:2184px;width:280px;font-size:10px;line-height:15px;color:#ddd}
.foot-about p+p{margin-top:8px}
.footer-base{left:0;top:2305px;width:1200px;height:29px;background:var(--footer-base);color:#ccc;font-size:10px;text-align:center;line-height:29px}
</style>
</head>
<body>

<header class="site-header abs">
  <div class="brand abs"><span class="brand-mark"></span><span class="brand-name">PlotLantern</span></div>
  <div class="field-sm abs" style="left:685px;top:12px;width:114px">Search Here</div>
  <div class="btn-sm abs" style="left:799px;top:12px;width:23px"><svg width="10" height="10" viewBox="0 0 10 10"><circle cx="4" cy="4" r="3" fill="none" stroke="#fff" stroke-width="1.4"/><path d="M6.2 6.2 9 9" stroke="#fff" stroke-width="1.4"/></svg></div>
  <div class="field-sm abs" style="left:836px;top:12px;width:80px">User name</div>
  <div class="btn-sm abs" style="left:918px;top:12px;width:54px">Login</div>
  <div class="btn-sm abs" style="left:986px;top:12px;width:52px">Sign up</div>
  <nav class="nav abs">
    <span style="left:772px">Briskline</span>
    <span style="left:884px">About</span>
    <span style="left:982px">Support</span>
  </nav>
</header>

<section class="hero abs" role="img" aria-label="Engineer in a hard hat using a smartphone in front of a construction crane"></section>
<div class="hero-arrow abs" style="left:124px"><svg width="32" height="32"><path d="M18 10l-6 6 6 6" fill="none" stroke="#333" stroke-width="2"/></svg></div>
<div class="hero-arrow abs" style="left:1040px"><svg width="32" height="32"><path d="M14 10l6 6-6 6" fill="none" stroke="#333" stroke-width="2"/></svg></div>
<div class="hero-band abs"></div>
<h1 class="hero-title abs">We provide all new experiences about product sales<br>data management services</h1>

<section>
  <h2 class="section-title welcome-title abs">Welcome to Plot Lantern</h2>
  <div class="title-rule abs" style="left:510px;top:758px;width:180px"></div>
  <p class="welcome-copy abs">Lorem ipsum dolor sit amet, consectetuer adipiscing elit, sed diam nonummy nibh euismod tincidunt ut laoreet dolore magna aliquam erat volutpat. Ut wisi enim ad minim veniam, quis nostrud exerci tation ullamcorper suscipit lobortis nisl ut aliquip ex ea commodo consequat. Duis autem vel eum iriure dolor in hendrerit in vulputate velit esse molestie consequat, vel illum dolore eu feugiat nulla facilisis at vero eros et accumsan et iusto odio dignissim qui blandit praesent luptatum zzril delenit augue duis dolore te feugait nulla facilisi.</p>
  <a class="btn-outline abs">Read More</a>
</section>

<section>
  <div class="work-band abs" role="img" aria-label="Construction workers in hard hats and safety vests, darkened"></div>
  <div class="signup-panel abs"></div>
  <h3 class="signup-title abs">Sign Up Now For Free!</h3>
  <div class="signup-input abs">enter email address</div>
  <a class="btn-primary signup-btn abs">Sign Up</a>
  <div class="video abs" role="img" aria-label="Video still of an excavator at a demolition site"></div>
  <h3 class="video-title abs">What We Do</h3>
  <svg class="abs" style="left:807px;top:1088px" width="36" height="36"><circle cx="18" cy="18" r="17" fill="rgba(0,0,0,.45)" stroke="#fff" stroke-width="2"/><path d="M14 11l11 7-11 7z" fill="#fff"/></svg>
  <div class="video-bar abs"></div>
  <svg class="abs" style="left:617px;top:1201px" width="416" height="14">
    <path d="M2 2l7 5-7 5z" fill="#fff"/>
    <text x="16" y="11" font-size="8" fill="#fff" font-family="Lato,sans-serif">04:08</text>
    <rect x="46" y="6" width="300" height="2" fill="#555"/><rect x="46" y="6" width="30" height="2" fill="#fff"/>
    <circle cx="76" cy="7" r="3" fill="#fff"/>
    <text x="354" y="11" font-size="8" fill="#fff" font-family="Lato,sans-serif">10:26</text>
    <path d="M384 5h3l4-3v10l-4-3h-3z" fill="#fff"/>
    <path d="M402 2l10 10M402 12l10-10" stroke="#fff" stroke-width="1.2"/>
  </svg>
</section>

<section>
  <div class="link-strip abs"></div>
  <a class="strip-btn store-btn abs"><span class="store-icon"></span><span><b>Get Briskline</b><small>from the Orbix App Bazaar</small></span></a>
  <a class="strip-btn abs" style="left:342px">See Our Pricing</a>
  <a class="strip-btn abs" style="left:521px">Case Studies</a>
  <a class="strip-btn abs" style="left:700px">About us</a>
  <a class="strip-btn abs" style="left:881px">Contact us</a>
</section>

<section>
  <div class="feature-area abs"></div>
  <h2 class="section-title feature-title abs">Product Feature</h2>
  <div class="title-rule abs" style="left:161px;top:1479px;width:426px"></div>
  <div class="tile abs" style="left:161px;top:1494px;background:linear-gradient(135deg,#7d5c3b,#d9d4c8 55%,#e3b72a)" role="img" aria-label="Tablet and hard hat on a desk"><span class="tile-caption">Lorem sum dolor sit amet.</span></div>
  <div class="tile abs" style="left:387px;top:1494px;background:linear-gradient(160deg,#a7bccd,#d7a530 50%,#7a6e5a)" role="img" aria-label="Excavator working on a site"><span class="tile-caption">Lorem sum dolor sit amet.</span></div>
  <div class="tile abs" style="left:161px;top:1675px;background:linear-gradient(135deg,#3c4450,#8c96a3 60%,#c9ced5)" role="img" aria-label="Hand pressing a digital keypad"><span class="tile-caption">Lorem sum dolor sit amet.</span></div>
  <div class="tile-text abs"><b>Lorem sum dolor sit amet.</b>Lorem sum dolor s consectetuer adipiscing elit, sed di nonummy nibh euismod tincidunt ut loreet re agn adipiscing elit.<span class="more">Read More &raquo;</span></div>

  <div class="progress abs"></div>
  <div class="progress-fill abs">24%</div>
  <label class="form-label abs" style="top:1496px">Company*</label><div class="form-field abs" style="top:1494px">Enter your Company Name</div>
  <label class="form-label abs" style="top:1533px">Name*</label><div class="form-field abs" style="top:1531px">Enter your Name</div>
  <label class="form-label abs" style="top:1570px">Email*</label><div class="form-field abs" style="top:1568px">Enter your Email Address</div>
  <label class="form-label abs" style="top:1609px">Phone*</label><div class="form-field abs" style="top:1607px">Enter your Phone no.</div>
  <div class="callback abs">Request Call back <i></i></div>
  <label class="form-label abs" style="top:1671px">How did you hear</label>
  <div class="form-field abs" style="top:1669px">Select<span class="select-caret abs"><svg width="28" height="27"><path d="M10 11h8l-4 5z" fill="#666"/></svg></span></div>
  <label class="form-label abs" style="top:1710px">Massages</label><div class="form-field abs" style="top:1708px;height:72px">Enter your Message</div>
  <a class="btn-primary submit-btn abs">Submit Query</a>
</section>

<section>
  <h2 class="section-title customers-title abs">Happy Customers Here</h2>
  <div class="title-rule abs" style="left:510px;top:1965px;width:180px"></div>
  <svg class="chev abs" style="left:236px" width="18" height="24"><path d="M14 2 4 12l10 10" fill="none" stroke="#ccc" stroke-width="3"/></svg>
  <svg class="chev abs" style="left:946px" width="18" height="24"><path d="M4 2l10 10L4 22" fill="none" stroke="#ccc" stroke-width="3"/></svg>
  <div class="avatar abs" role="img" aria-label="Portrait photo of a smiling customer"></div>
  <blockquote class="quote abs">Lorem ipsum dolor sit amet, consectetur adipiscing elit. Integer venenatis tincidunt elit, aliquam semper quam pulvinar id. Aliquam erat volutpat. Integer nulla urna, sagittis sed viverra quis, tincidunt vel felis. Pellentesque eleifend sem ut diam bibendum, non sagittis sapien pellentesque. Etiam semper<b>Lorem ipsum dolor sit amet</b></blockquote>
</section>

<footer>
  <div class="site-footer abs"></div>
  <div class="foot-col abs" style="left:163px"><h4>About</h4><ul><li>Company</li><li>Press</li></ul></div>
  <div class="foot-col abs" style="left:311px"><h4>Briskline</h4><ul><li>Product</li><li>Pricing</li><li>Case Studies</li></ul></div>
  <div class="foot-col abs" style="left:461px"><h4>Support</h4><ul><li>Contact us</li><li>Terms of use</li><li>Privacy</li><li>Help</li></ul></div>
  <div class="foot-col abs" style="left:611px"><h4>Download</h4><ul><li>Orbix Mobile</li></ul></div>
  <div class="social abs"><i></i><i></i><i></i><i></i></div>
  <div class="foot-about abs"><p>Lorem ipsum dolor sit amet, maiores ornare fermentum imperdiet ut vivamus a, nam lectus at Quam euismo sein semper ut potenti pellentesque quisque.</p><p>Mperdiet ut vivamus a, nam lectus at Quam euismo sein Lorem ipsum dolor sit amet, maiores.</p></div>
  <div class="footer-base abs">Copyright &copy; 2014 PlotLantern. All Rights Reserved</div>
</footer>

</body>
</html>
```